Holistic Health Coach needs simple web site design for a new practice

I need a web (re)design for my entire site, Birchwell Sprout Lady. I have a beautiful new blue and green logo that I'd like the site fonts and color scheme to be built around. I'll attach my new logo so you'll know the colors/design feel I'm after.

I want easy navigation for my mostly text based site, widgets for my social media pages and a clean, fun, light feel for the site.

Target Market(s)

People looking to take charge of their own health, and who may need my coaching services to obtain optimal wellness.

Industry/Entity Type

Health

Coding

Coded - Design and coding required

Number of Pages Required

5+ page

Font styles to use
Script

Colors
33b8a4
33a6d7
ffffff

Requirements
Must have
• Must incorporate my logo design, as well as same/similar fonts and color scheme.
• I'd like it to stay as close to the current design as possible.
Nice to have
• Would love to incorporate a hover over menu (for example, when a user hovers over "About", they will see the submenu in a floating design.
Should not have
• No dark colors or masculine feel

```html
<!DOCTYPE html>
<html lang="en">
<head>
<meta charset="utf-8">
<title>Birchwell Sprout Lady – Blog</title>
<link href="https://fonts.googleapis.com/css2?family=Open+Sans:wght@400;600&family=Roboto+Slab:wght@700&family=Dancing+Script:wght@500&display=swap" rel="stylesheet">
<style>
:root{
  --page:#f2f2f2;
  --card:#ffffff;
  --border:#dcdcdc;
  --text:#555555;
  --heading:#3a3a3a;
  --muted:#9a9a9a;
  --link:#e0413b;
  --teal:#33b8a4;
  --blue:#33a6d7;
  --green:#8cc63f;
  --footer:#062b3a;
}
*{box-sizing:border-box;margin:0;padding:0}
html,body{width:800px;height:1200px;overflow:hidden}
body{background:var(--page);font-family:"Open Sans",Arial,sans-serif;font-size:8.1px;line-height:13.6px;color:var(--text);position:relative}
a{color:var(--link);text-decoration:none}

.post{position:absolute;left:78px;width:427px;background:var(--card);border:1px solid var(--border);border-radius:3px;padding:0 30px}
.post p{margin:0 0 6px}
.post-title{font-family:"Roboto Slab",Georgia,serif;font-weight:700;font-size:16.5px;line-height:22px;color:var(--heading)}
.post-meta{display:flex;gap:12px;font-size:7.6px;color:var(--muted);margin:9px 0 14px}
.post-meta span{display:flex;align-items:center;gap:4px}
.rule{width:34px;height:1px;background:var(--border);margin:8px 0 6px}
.read-more{display:inline-block;background:var(--teal);color:#fff;font-family:Georgia,serif;font-size:8.2px;width:60px;height:24px;line-height:24px;text-align:center;border-radius:2px}
.share-label{color:var(--link);font-family:Georgia,serif;font-weight:700;font-size:7px;margin:9px 0 3px}
.share{display:flex;gap:3px}
.share span{display:flex;align-items:center;gap:3px;height:14px;padding:0 4px;border:1px solid #cfcfcf;border-radius:2px;font-size:7px;color:#555;background:#fafafa}
.share i{display:inline-block;width:6px;height:6px;background:#666;border-radius:1px}
.share svg{width:7px;height:7px}
.poster{display:block;width:169px;height:141px;margin:18px auto 17px;background:linear-gradient(160deg,#f6c3ca,#f0b4bd)}

.widget{position:absolute;left:521px;width:186px;background:var(--card);border:1px solid var(--border);border-radius:3px;padding:0 10px}
.widget-title{font-family:"Dancing Script",cursive;font-weight:500;color:var(--green);font-size:16px;text-align:center;margin-top:10px;line-height:22px}
.divider{display:flex;align-items:center;gap:4px;margin:5px 0 12px}
.divider .line{flex:1;height:1px;background:#c8c8c8}
.divider .flourish{width:62px;height:10px;border-radius:5px;background:linear-gradient(90deg,#e6e6e6,#cfcfcf,#e6e6e6)}
.widget ul{list-style:none}
.widget li{font-size:7.8px;line-height:11.4px;color:var(--muted);padding:5px 0 6px;border-bottom:1px solid #ebebeb}
.widget li:last-child{border-bottom:0}
.icon-list li{display:flex;gap:8px;align-items:center;padding:5px 0 6px 0}
.icon-list svg{flex:none;width:10px;height:10px}
.comments li{display:flex;gap:6px;align-items:flex-start;color:var(--muted);padding:3px 0 12px;margin-bottom:6px}
.comments li svg{flex:none;width:10px;height:9px;margin-top:2px}
.comments .author{color:#555}

.pager{position:absolute;left:81px;top:1106px;display:flex;gap:5px}
.pager span{background:var(--blue);color:#fff;font-family:Georgia,serif;font-size:7.6px;height:22px;line-height:22px;padding:0 9px;border-radius:2px}

.site-footer{position:absolute;left:0;top:1153px;width:800px;height:47px;background:var(--footer);color:#fff;font-size:7.4px;text-align:center;line-height:47px}
.site-footer a{color:var(--teal)}
</style>
</head>
<body>

<article class="post" style="top:-30px;height:385px;padding-top:26px">
  <p>exercise while recovering, and some solid reasons why overtraining is detrimental to your health as well.</p>
  <p>Whew – that was a lot in one module, huh? I didn't realize how much I'd learned until I started typing it all out here. My hope is that you something in this article strikes a chord with you and leaves wanting to learn more about this program. I cannot say enough good things about it. I wasn't sure I'd really feel better in just a few short weeks, and to be fair, they said from the outset that no one would be completely recovered in our time together, but the changes I've made are already making a difference.</p>
  <p>I can't wait to see what the Bonus Module holds for me (us) next week. Until then, have a great weekend and take care of yourself and your body 🙂</p>
  <p style="margin-top:11px">My thoughts on <a href="#">Module 1</a></p>
  <p>My thoughts on <a href="#">Module 2</a></p>
  <p>My thoughts on <a href="#">Module 3</a></p>
  <p>Check out Nora Whitfield on <a href="#">Friendbook</a>, <a href="#">Chirper</a>, <a href="#">Snapgram</a>, and her <a href="#">website</a></p>
  <p>Check out Tessa Brannock on <a href="#">Friendbook</a>, <a href="#">Chirper</a>, and her <a href="#">website</a></p>
  <div class="rule"></div>
  <a class="read-more" href="#">Read More</a>
  <div class="share-label">Share this:</div>
  <div class="share">
    <span><svg viewBox="0 0 8 8"><rect x="0" y="1.5" width="8" height="5" fill="#666"/><path d="M0 1.5 4 4.5 8 1.5" stroke="#fff" fill="none" stroke-width=".8"/></svg>Email</span>
    <span><svg viewBox="0 0 8 8"><rect x="2" y="0" width="4" height="3" fill="#666"/><rect x="0" y="3" width="8" height="3" fill="#666"/><rect x="2" y="5" width="4" height="3" fill="#999"/></svg>Print</span>
    <span><i></i>Friendbook</span>
    <span><i></i>Chirper</span>
    <span><i></i>Globe+</span>
    <span><i></i>Pinboard</span>
  </div>
</article>

<article class="post" style="top:368px;height:431px;padding-top:15px">
  <h2 class="post-title">April Essential Living Education Series</h2>
  <div class="post-meta">
    <span><svg width="8" height="8" viewBox="0 0 8 8"><rect x="0" y="1" width="8" height="7" fill="#5aa0c8"/><rect x="1" y="3" width="6" height="4" fill="#fff"/></svg>April 5, 2015</span>
    <span><svg width="8" height="8" viewBox="0 0 8 8"><ellipse cx="4" cy="3.5" rx="3.6" ry="3" fill="none" stroke="#5aa0c8"/></svg>Leave a comment</span>
  </div>
  <p>During the month of April, I will be doing a series of Friendbook classes designed with you in mind. Topics range from skin care and personal care to Healing Oils of the Bible, Hormones, and how to have a Chemical Free Home.</p>
  <div class="poster" role="img" aria-label="Pink class schedule graphic listing six April classes: Verdant Living Skincare, Verdant Living Personal Care, Next Step Oils, Healing Oils of the Bible, Chemical Free Home, Taming the Dragon Within – Essential Living Education Series"></div>
  <p>I hope you can join me for some fun educational Friendbook classes!! Please let me know what other classes you'd like to see 🙂</p>
  <div style="height:13px"></div>
  <a class="read-more" href="#">Read More</a>
  <div class="share-label" style="margin-top:4px">Share this:</div>
  <div class="share">
    <span><svg viewBox="0 0 8 8"><rect x="0" y="1.5" width="8" height="5" fill="#666"/><path d="M0 1.5 4 4.5 8 1.5" stroke="#fff" fill="none" stroke-width=".8"/></svg>Email</span>
    <span><svg viewBox="0 0 8 8"><rect x="2" y="0" width="4" height="3" fill="#666"/><rect x="0" y="3" width="8" height="3" fill="#666"/><rect x="2" y="5" width="4" height="3" fill="#999"/></svg>Print</span>
    <span><i></i>Friendbook</span>
    <span><i></i>Chirper</span>
    <span><i></i>Globe+</span>
    <span><i></i>Pinboard</span>
  </div>
</article>

<article class="post" style="top:813px;height:279px;padding-top:15px">
  <h2 class="post-title">April Essential Living Education Series</h2>
  <div class="post-meta">
    <span><svg width="8" height="8" viewBox="0 0 8 8"><rect x="0" y="1" width="8" height="7" fill="#5aa0c8"/><rect x="1" y="3" width="6" height="4" fill="#fff"/></svg>April 5, 2015</span>
    <span><svg width="8" height="8" viewBox="0 0 8 8"><ellipse cx="4" cy="3.5" rx="3.6" ry="3" fill="none" stroke="#5aa0c8"/></svg>Leave a comment</span>
  </div>
  <p>During the month of April, I will be doing a series of Friendbook classes designed with you in mind. Topics range from skin care and personal care to Healing Oils of the Bible, Hormones, and how to have a Chemical Free Home.</p>
  <p style="margin-top:12px">I hope you can join me for some fun educational Friendbook classes!! Please let me know what other classes you'd like to see 🙂</p>
  <div class="rule" style="margin-top:14px"></div>
  <a class="read-more" href="#">Read More</a>
  <div class="share-label">Share this:</div>
  <div class="share">
    <span><svg viewBox="0 0 8 8"><rect x="0" y="1.5" width="8" height="5" fill="#666"/><path d="M0 1.5 4 4.5 8 1.5" stroke="#fff" fill="none" stroke-width=".8"/></svg>Email</span>
    <span><svg viewBox="0 0 8 8"><rect x="2" y="0" width="4" height="3" fill="#666"/><rect x="0" y="3" width="8" height="3" fill="#666"/><rect x="2" y="5" width="4" height="3" fill="#999"/></svg>Print</span>
    <span><i></i>Friendbook</span>
    <span><i></i>Chirper</span>
    <span><i></i>Globe+</span>
    <span><i></i>Pinboard</span>
  </div>
</article>

<nav class="pager"><span>◂ Older Post</span><span>New Post ▸</span></nav>

<aside class="widget" style="top:9px;height:221px">
  <h3 class="widget-title">Recent Posts</h3>
  <div class="divider"><span class="line"></span><span class="flourish" role="img" aria-label="Decorative scroll flourish"></span><span class="line"></span></div>
  <ul>
    <li>Lifestyles of the Tired and Wired – Module 4 of Calm Roots Reset: Adrenal Fatigue</li>
    <li>April Essential Living Education Series</li>
    <li>Module 3: A Nice Supplement to the Program</li>
    <li>What Do You Mean I Can't Have Coffee?!? – Module 2 Calm Roots Reset: Adrenal Fatigue</li>
    <li>DIY Emotional Regulation Blend</li>
  </ul>
</aside>

<aside class="widget" style="top:244px;height:322px">
  <h3 class="widget-title">Recent Comments</h3>
  <div class="divider"><span class="line"></span><span class="flourish" role="img" aria-label="Decorative scroll flourish"></span><span class="line"></span></div>
  <ul class="comments">
    <li><svg viewBox="0 0 10 9"><ellipse cx="5" cy="4" rx="4.4" ry="3.4" fill="none" stroke="#33a6d7" stroke-width="1.2"/></svg><div><span class="author">Lifestyles of the Tired and Wired – Module 4 of Calm Roots Reset: Adrenal Fatigue | Birchwell Sprout Lady</span> on What Do You Mean I Can't Have Coffee?!? – Module 2 Calm Roots Reset: Adrenal Fatigue</div></li>
    <li><svg viewBox="0 0 10 9"><ellipse cx="5" cy="4" rx="4.4" ry="3.4" fill="none" stroke="#33a6d7" stroke-width="1.2"/></svg><div><span class="author">Lifestyles of the Tired and Wired – Module 4 of Calm Roots Reset: Adrenal Fatigue | Birchwell Sprout Lady</span> on What Do You Mean I Can't Have Coffee?!? – Module 2 Calm Roots Reset: Adrenal Fatigue</div></li>
    <li><svg viewBox="0 0 10 9"><ellipse cx="5" cy="4" rx="4.4" ry="3.4" fill="none" stroke="#33a6d7" stroke-width="1.2"/></svg><div><span class="author">Lifestyles of the Tired and Wired – Module 4 of Calm Roots Reset: Adrenal Fatigue | Birchwell Sprout Lady</span> on What Do You Mean I Can't Have Coffee?!? – Module 2 Calm Roots Reset: Adrenal Fatigue</div></li>
  </ul>
</aside>

<aside class="widget" style="top:580px;height:262px">
  <h3 class="widget-title">Archives</h3>
  <div class="divider"><span class="line"></span><span class="flourish" role="img" aria-label="Decorative scroll flourish"></span><span class="line"></span></div>
  <ul class="icon-list">
    <li><svg viewBox="0 0 10 10"><rect x="0" y="1" width="10" height="9" fill="#5aa0c8"/><rect x="1.3" y="3.5" width="7.4" height="5.2" fill="#fff"/></svg>April 2015</li>
    <li><svg viewBox="0 0 10 10"><rect x="0" y="1" width="10" height="9" fill="#5aa0c8"/><rect x="1.3" y="3.5" width="7.4" height="5.2" fill="#fff"/></svg>March 2015</li>
    <li><svg viewBox="0 0 10 10"><rect x="0" y="1" width="10" height="9" fill="#5aa0c8"/><rect x="1.3" y="3.5" width="7.4" height="5.2" fill="#fff"/></svg>February 2015</li>
    <li><svg viewBox="0 0 10 10"><rect x="0" y="1" width="10" height="9" fill="#5aa0c8"/><rect x="1.3" y="3.5" width="7.4" height="5.2" fill="#fff"/></svg>January 2015</li>
    <li><svg viewBox="0 0 10 10"><rect x="0" y="1" width="10" height="9" fill="#5aa0c8"/><rect x="1.3" y="3.5" width="7.4" height="5.2" fill="#fff"/></svg>September 2014</li>
    <li><svg viewBox="0 0 10 10"><rect x="0" y="1" width="10" height="9" fill="#5aa0c8"/><rect x="1.3" y="3.5" width="7.4" height="5.2" fill="#fff"/></svg>June 2014</li>
    <li><svg viewBox="0 0 10 10"><rect x="0" y="1" width="10" height="9" fill="#5aa0c8"/><rect x="1.3" y="3.5" width="7.4" height="5.2" fill="#fff"/></svg>May 2014</li>
    <li><svg viewBox="0 0 10 10"><rect x="0" y="1" width="10" height="9" fill="#5aa0c8"/><rect x="1.3" y="3.5" width="7.4" height="5.2" fill="#fff"/></svg>April 2014</li>
  </ul>
</aside>

<aside class="widget" style="top:856px;height:234px">
  <h3 class="widget-title">Categories</h3>
  <div class="divider"><span class="line"></span><span class="flourish" role="img" aria-label="Decorative scroll flourish"></span><span class="line"></span></div>
  <ul class="icon-list">
    <li><svg viewBox="0 0 10 10"><path d="M0.5 2h3l1 1.2h5v5.3h-9z" fill="none" stroke="#5aa0c8"/></svg>21 Day Sweet Reset</li>
    <li><svg viewBox="0 0 10 10"><path d="M0.5 2h3l1 1.2h5v5.3h-9z" fill="none" stroke="#5aa0c8"/></svg>Adrenal Fatigue</li>
    <li><svg viewBox="0 0 10 10"><path d="M0.5 2h3l1 1.2h5v5.3h-9z" fill="none" stroke="#5aa0c8"/></svg>Articles</li>
    <li><svg viewBox="0 0 10 10"><path d="M0.5 2h3l1 1.2h5v5.3h-9z" fill="none" stroke="#5aa0c8"/></svg>DIY</li>
    <li><svg viewBox="0 0 10 10"><path d="M0.5 2h3l1 1.2h5v5.3h-9z" fill="none" stroke="#5aa0c8"/></svg>Essential Oils</li>
    <li><svg viewBox="0 0 10 10"><path d="M0.5 2h3l1 1.2h5v5.3h-9z" fill="none" stroke="#5aa0c8"/></svg>Real Food</li>
    <li><svg viewBox="0 0 10 10"><path d="M0.5 2h3l1 1.2h5v5.3h-9z" fill="none" stroke="#5aa0c8"/></svg>Uncategorized</li>
  </ul>
</aside>

<footer class="site-footer"><a href="#">Birchwell Sprout Lady</a> All Rights Reserved. Theme by <a href="#">Meadow Themes</a> Powered by <a href="#">PressPage</a></footer>

</body>
</html>
```